Fold up small biz card size flyer for Waxing Salon

To design a simple informative flyer which can fold 3 times measuring 2" x 9" for Waxing Salon in Toronto ON CanadaMy client would like both sides of flyer to have text i.e. the first half of flyer text on front and second half with address etc on back.She doesn;t want a company name as yet but would like maybe the simple shape of a body as in this sample deisign with a stone background.the other pics are just samples of ideas she has suggessted and if there is any text it should simply be wax or waxing or maybe body waxing.Please don't hesitate to ask quesition and i look forward to your submissions.

Target Market(s)

women amd men of all adult ages

Font styles to use
Serif
Sans Serif
Decorative
Script

Colors

Designer to choose colors to be used in the design.

Requirements
Must have
• Fold into three to biz card size so PLEASE STRICTLY 2 INCHES X 9 INCHES AND FOLDED DOWN TO A 2 X 3 BIZ CARD
• Due to small size of flyer there will have to be text on back as well
• thanks for your time and patience
Nice to have
• the images are simply ideas of existing brands...just stone background with perhadps small body shaped graphic no company name
Should not have
• scanitly clad women preferably small body shoped graphic only please/

```html
<!DOCTYPE html>
<html lang="en">
<head>
<meta charset="utf-8">
<title>Waxing Salon Fold Flyer</title>
<link rel="stylesheet" href="https://fonts.googleapis.com/css2?family=Catamaran:wght@300;400;500;600;700;800;900&display=swap">
<style>
  :root {
    --orange: #f26f1f;
    --yellow: #fcc417;
    --red: #e8202a;
    --ink: #231f20;
    --ink-warm: #3a2414;
    --paper: #f3f2f0;
    --stage: #e8e4df;
    --white: #ffffff;
  }
  * { box-sizing: border-box; margin: 0; padding: 0; }
  html, body { width: 1200px; height: 1200px; overflow: hidden; }
  body {
    background: var(--stage);
    font-family: "Catamaran", sans-serif;
    color: var(--ink);
    position: relative;
  }
  .panel {
    position: absolute;
    top: 28px;
    width: 254px;
    height: 1144px;
    background: var(--paper);
    overflow: hidden;
    box-shadow: 0 6px 18px rgba(0,0,0,.18);
  }
  .panel--front { left: 277px; }
  .panel--back { left: 668px; }
  .panel > * { position: absolute; }

  .header-bg { top: 0; left: 0; width: 254px; height: 180px; }
  .headline-text {
    font-family: "Catamaran", sans-serif;
    font-weight: 900;
    fill: var(--red);
    stroke: var(--white);
    stroke-width: 3px;
    paint-order: stroke;
    stroke-linejoin: round;
  }

  .offer { display: flex; align-items: flex-start; }
  .offer__price {
    color: var(--red);
    font-weight: 700;
    font-size: 78px;
    line-height: .8;
    letter-spacing: -3px;
  }
  .offer__price sup { font-size: 28px; vertical-align: top; position: relative; top: -2px; margin-right: 3px; letter-spacing: 0; }
  .offer__name {
    font-size: 31px;
    font-weight: 500;
    line-height: .98;
    color: #2c2c2c;
    margin-left: 8px;
    margin-top: -4px;
  }
  .value { left: 24px; top: 252px; font-size: 20px; font-style: italic; font-weight: 600; white-space: nowrap; }
  .value small { font-size: 13.5px; font-weight: 400; }
  .accent { color: var(--red); font-weight: 600; font-size: 21px; line-height: 25.5px; left: 22px; white-space: nowrap; }
  .lead { left: 22px; top: 310px; font-size: 21px; font-weight: 600; line-height: 25.5px; white-space: nowrap; }
  .details { left: 21px; top: 446px; font-size: 14.6px; font-weight: 400; line-height: 17.6px; white-space: nowrap; }

  .cta-band { left: 0; top: 0; width: 254px; height: 1144px; }
  .cta-text { font-family: "Catamaran", sans-serif; font-weight: 700; font-size: 28px; fill: var(--white); }

  .location {
    left: 0; width: 254px; text-align: center;
    color: var(--ink-warm); font-weight: 600; font-size: 15px; line-height: 17.6px; font-style: normal;
  }
  .location em { font-weight: 400; font-size: 12px; line-height: 14.5px; display: block; font-style: italic; }
  .divider { left: 33px; top: 969px; width: 188px; height: 1px; background: rgba(255,255,255,.75); }

  .condition { left: 0; width: 254px; text-align: center; top: 248px; font-size: 13px; font-style: italic; line-height: 17px; }
  .services {
    left: 20px; top: 298px; list-style: none;
    font-size: 15.4px; font-weight: 400; line-height: 20.25px;
  }
  .services li { display: flex; white-space: nowrap; }
  .services .num { width: 24px; text-align: right; margin-right: 9px; }
  .note { left: 21px; top: 940px; font-size: 11.5px; line-height: 14.5px; }
  .note strong { font-weight: 700; }
  .share-box {
    left: 0; top: 1023px; width: 254px; height: 71px;
    background: var(--red); color: var(--white);
    text-align: center; font-weight: 600; font-size: 15px; line-height: 17.6px;
    padding-top: 9px;
    box-shadow: 0 -3px 6px rgba(0,0,0,.08);
  }
  .fine-print { left: 0; width: 254px; top: 1108px; text-align: center; font-size: 13.5px; font-style: italic; }
</style>
</head>
<body>

<section class="panel panel--front">
  <svg class="header-bg" viewBox="0 0 254 180" aria-hidden="true">
    <defs>
      <radialGradient id="burstFront" cx="0.7" cy="0.75" r="0.85">
        <stop offset="0" stop-color="#ffd21a"/>
        <stop offset="0.45" stop-color="#f9a51c"/>
        <stop offset="1" stop-color="#f06a1e"/>
      </radialGradient>
    </defs>
    <rect width="254" height="180" fill="url(#burstFront)"/>
    <path d="M0 140 C70 160 160 146 254 120 L254 130 C160 156 70 170 0 150 Z" fill="#ffe27a"/>
    <path d="M0 150 C70 170 160 156 254 128 L254 180 L0 180 Z" fill="var(--paper)"/>
    <text class="headline-text" x="15" y="84" font-size="30" textLength="189" lengthAdjust="spacingAndGlyphs" transform="rotate(-18 15 84)">DOORBUSTER</text>
    <text class="headline-text" x="63" y="132" font-size="86" textLength="180" lengthAdjust="spacingAndGlyphs" transform="rotate(-18 63 132)">DEAL</text>
  </svg>

  <div class="offer" style="top:188px; left:22px">
    <div class="offer__price"><sup>$</sup>66</div>
    <div class="offer__name">Body<br>Waxing</div>
  </div>
  <p class="value">$120 value! <small>For women only</small></p>
  <p class="accent" style="top:285px">Neck to Toe.</p>
  <p class="lead">Including Brazilian<br>with Take Home<br>Scrub used to<br>improve in-grown<br>body hair.</p>
  <p class="details">Guests receive full body<br>waxing during one<br>appointment on the following<br>areas: butt, hollywood, bikini,<br>underarms, stomach, cleavage,<br>full back, full arms &amp; full legs.</p>

  <div class="offer" style="top:589px; left:22px">
    <div class="offer__price"><sup>$</sup>66</div>
    <div class="offer__name">Body<br>Polishing</div>
  </div>
  <p class="accent" style="top:657px">The secret to soft,<br>smooth skin.</p>

  <svg class="cta-band" viewBox="0 0 254 1144" aria-hidden="true">
    <defs>
      <radialGradient id="burstBottom" cx="0.55" cy="0.15" r="0.9">
        <stop offset="0" stop-color="#ffd01a"/>
        <stop offset="0.4" stop-color="#f8981c"/>
        <stop offset="1" stop-color="#ef5e1d"/>
      </radialGradient>
    </defs>
    <path d="M0 831 L254 778 L254 1144 L0 1144 Z" fill="url(#burstBottom)"/>
    <path d="M0 752 L254 699 L254 778 L0 831 Z" fill="var(--red)"/>
    <text class="cta-text" x="137" y="768" text-anchor="middle" transform="rotate(-12 137 768)">Call today</text>
    <text class="cta-text" x="122" y="797" text-anchor="middle" transform="rotate(-12 122 797)">to book a spot.</text>
  </svg>

  <address class="location" style="top:839px">
    2150 Maple Grove Ave<br>#3 Toronto<br>ON M6P 3K8
    <em>Opp to Saffron Grill</em>
    (416) 555-0142<br>1 (833) 555-0198
  </address>
  <div class="divider"></div>
  <address class="location" style="top:985px">
    880 Cedarbrook Rd<br>#3 North York<br>ON M2R 4T5
    <em>Opp to Northgate Mall<br>Next to Quickway</em>
    (416) 555-0176<br>1 (833) 555-0123
  </address>
</section>

<section class="panel panel--back">
  <svg class="header-bg" viewBox="0 0 254 180" aria-hidden="true">
    <defs>
      <radialGradient id="burstBack" cx="0.6" cy="0.8" r="0.85">
        <stop offset="0" stop-color="#ffd21a"/>
        <stop offset="0.45" stop-color="#f9a51c"/>
        <stop offset="1" stop-color="#f06a1e"/>
      </radialGradient>
    </defs>
    <rect width="254" height="180" fill="url(#burstBack)"/>
    <path d="M0 140 C70 160 160 146 254 120 L254 130 C160 156 70 170 0 150 Z" fill="#ffe27a"/>
    <path d="M0 150 C70 170 160 156 254 128 L254 180 L0 180 Z" fill="var(--paper)"/>
    <text class="headline-text" x="19" y="81" font-size="30" textLength="180" lengthAdjust="spacingAndGlyphs" transform="rotate(-18 19 81)">UNBEATABLE</text>
    <text class="headline-text" x="46" y="128" font-size="80" textLength="186" lengthAdjust="spacingAndGlyphs" transform="rotate(-18 46 128)">VALUE</text>
  </svg>

  <div class="offer" style="top:196px; left:32px">
    <div class="offer__price" style="font-size:68px"><sup>$</sup>13</div>
    <div class="offer__name" style="font-size:25px; margin-top:-2px">Spa<br>Treatments</div>
  </div>
  <p class="condition">when you purchase 5 or<br>more services from list below</p>

  <ol class="services">
    <li><span class="num">1.</span>Back Massage</li>
    <li><span class="num">2.</span>Back Scrub</li>
    <li><span class="num">3.</span>Spa Manicure</li>
    <li><span class="num">4.</span>Full Brazilian Wax</li>
    <li><span class="num">5.</span>Full 60 Minute Facial</li>
    <li><span class="num">6.</span>Face Polishing</li>
    <li><span class="num">7.</span>Face Bleaching</li>
    <li><span class="num">8.</span>Scalp &amp; Hair Oil Massage</li>
    <li><span class="num">9.</span>Dry Hair Treatment</li>
    <li><span class="num">10.</span>Hair Colour Application</li>
    <li><span class="num">11.</span>Four Inch Henna Tattoo</li>
    <li><span class="num">12.</span>Eyebrow Tinting/Shaping</li>
    <li><span class="num">13.</span>Upper Lip Thread/wax</li>
    <li><span class="num">14.</span>Forehead Thread/wax</li>
    <li><span class="num">15.</span>Side Burn Thread/Wax</li>
    <li><span class="num">16.</span>Full Face Thread/Wax</li>
    <li><span class="num">17.</span>Nostril Wax</li>
    <li><span class="num">18.</span>Nape Wax</li>
    <li><span class="num">19.</span>Cleavage Wax</li>
    <li><span class="num">20.</span>Stomach Wax</li>
    <li><span class="num">21.</span>Upper Back Wax</li>
    <li><span class="num">22.</span>Lower Back Wax</li>
    <li><span class="num">23.</span>Underarm Wax</li>
    <li><span class="num">24.</span>Half Arm Wax</li>
    <li><span class="num">25.</span>Full Arm Wax</li>
    <li><span class="num">26.</span>Half Legs Wax</li>
    <li><span class="num">27.</span>Full Legs Wax</li>
    <li><span class="num">28.</span>Bikini Line Wax</li>
    <li><span class="num">29.</span>Bum Wax</li>
    <li><span class="num">30.</span>Hollywood Wax</li>
  </ol>

  <p class="note"><strong>Note:</strong><br>#3 $5 extra for nail polish<br>#4 counts as 2 services<br>#5 counts as 3 services</p>
  <p class="share-box">Services may be<br>Shared with your<br>Loved Ones</p>
  <p class="fine-print">Some conditions apply</p>
</section>

</body>
</html>
```